Etiquette pour pots de Miel de Kolvera
Besoins
Nous souhaitons créer une étiquette pour notre Miel de Kolvera, produit et commercialisé en République Démocratique du Congo.
Ce miel s’apparente à une qualité bio car les ruches se trouvent en pleine nature, loin des villes et de la pollution.
Les caractéristiques du flacon sont les suivantes (photo ci-joint) :
Hauteur : 12 cm
Circonférence (mi-hauteur) : 34 cm
Diamètre (ouverture supérieure) : 8 cm
Contenance : 660 ml.
La taille de l’étiquette est laissée à la libre appréciation du graphiste.
L’étiquette doit évoquer le côté sain/circuit court/bio et la qualité.
Les éléments suivants doivent être présents sur l’étiquette :
1. Nom du produit :
MIEL DE KOLVERA
ASALI YA KOLVERA (traduction en swahili)
2. Eléments : abeille stylisée, fleurs
3. Logo Tumsoa (ci-joint)
4. Producteur : Ranch de Kolvera
5. Miel Bio des plateaux de Kolvera
6. 660 ml

```html
<!DOCTYPE html>
<html lang="fr">
<head>
<meta charset="utf-8">
<title>Miel de Kolvera – Étiquettes</title>
<link rel="stylesheet" href="https://fonts.googleapis.com/css2?family=Great+Vibes&family=PT+Sans:wght@400;700&display=swap">
<style>
  :root {
    --backdrop: #776b5f;
    --ink-brown: #4b2a1d;
    --brand-green: #7a9a3c;
    --cream-band: #e6e3dc;
    --cream-edge: #e2ddd3;
    --honey-band: #f5d11e;
    --honey-edge: #f4cf1c;
    --label-white: #ffffff;
    --dash-line: #b8ab98;
  }
  * { margin: 0; padding: 0; box-sizing: border-box; }
  html, body { width: 1200px; height: 1128px; overflow: hidden; }
  body { background: var(--backdrop); font-family: "PT Sans", Arial, sans-serif; color: var(--ink-brown); }
  .canvas { position: relative; width: 1200px; height: 1128px; }
  .label { position: absolute; left: 0; width: 1200px; height: 564px; }
  .label--cream { top: 0; }
  .label--honey { top: 566px; }
  .label-shape { position: absolute; inset: 0; }
  .bee-mark {
    position: absolute; left: 540px; top: 88px; width: 120px; height: 130px;
    border-radius: 50% 50% 46% 46%; background: var(--ink-brown); opacity: .85;
  }
  .bee-small {
    position: absolute; left: 716px; top: 108px; width: 42px; height: 48px;
    border-radius: 50%; background: var(--ink-brown); opacity: .8;
  }
  .product-name {
    position: absolute; left: 0; right: 0; top: 250px; text-align: center;
    font-family: "Great Vibes", cursive; font-size: 100px; line-height: 1; font-weight: 400;
  }
  .product-swahili {
    position: absolute; left: 0; right: 0; top: 362px; text-align: center;
    font-size: 23px; letter-spacing: .5px; line-height: 1;
  }
  .producer-brand {
    position: absolute; left: 0; right: 0; top: 404px; text-align: center;
    font-size: 15px; font-weight: 700; letter-spacing: 1.5px; color: var(--brand-green); line-height: 1;
    display: flex; justify-content: center; align-items: center; gap: 8px;
  }
  .producer-brand .dot { width: 12px; height: 12px; border-radius: 50%; background: var(--brand-green); }
  .product-origin {
    position: absolute; left: 0; right: 0; top: 436px; text-align: center;
    font-size: 23px; line-height: 30px;
  }
  .volume {
    position: absolute; left: 0; right: 0; top: 508px; text-align: center;
    font-size: 11px; line-height: 1; display: flex; justify-content: center; align-items: center; gap: 8px;
  }
  .volume .rule { width: 34px; height: 1px; background: var(--ink-brown); }
</style>
</head>
<body>
<main class="canvas">

  <section class="label label--cream">
    <svg class="label-shape" width="1200" height="564" viewBox="0 0 1200 564">
      <defs>
        <radialGradient id="creamGlow" cx="50%" cy="50%" r="50%">
          <stop offset="0" stop-color="#ffffff"/>
          <stop offset=".6" stop-color="#f6f5f1"/>
          <stop offset="1" stop-color="#e2ddd3"/>
        </radialGradient>
      </defs>
      <rect x="72" y="212" width="1058" height="142" fill="var(--cream-band)"/>
      <ellipse cx="600" cy="280" rx="390" ry="268" fill="url(#creamGlow)"/>
      <ellipse cx="600" cy="280" rx="376" ry="254" fill="none" stroke="var(--dash-line)" stroke-width="1.2" stroke-dasharray="3 4"/>
    </svg>
    <div class="bee-mark" role="img" aria-label="Abeille stylisée"></div>
    <div class="bee-small" role="img" aria-label="Petite abeille en vol"></div>
    <h1 class="product-name">Miel de Kolvera</h1>
    <p class="product-swahili">ASALI YA KOLVERA</p>
    <p class="producer-brand"><span class="dot"></span>TUMSOA</p>
    <p class="product-origin">Miel Bio des plateaux de Kolvera<br>issue du Ranch de Kolvera</p>
    <p class="volume"><span class="rule"></span>660ml<span class="rule"></span></p>
  </section>

  <section class="label label--honey">
    <svg class="label-shape" width="1200" height="564" viewBox="0 0 1200 564">
      <defs>
        <radialGradient id="honeyGlow" cx="50%" cy="50%" r="50%">
          <stop offset="0" stop-color="#ffffff"/>
          <stop offset=".45" stop-color="#fdf3c4"/>
          <stop offset="1" stop-color="#f4cf1c"/>
        </radialGradient>
      </defs>
      <rect x="72" y="212" width="1058" height="142" fill="var(--honey-band)"/>
      <ellipse cx="600" cy="280" rx="390" ry="268" fill="url(#honeyGlow)"/>
      <ellipse cx="600" cy="280" rx="376" ry="254" fill="none" stroke="#d8b61a" stroke-width="1.2" stroke-dasharray="3 4"/>
    </svg>
    <div class="bee-mark" role="img" aria-label="Abeille stylisée"></div>
    <div class="bee-small" role="img" aria-label="Petite abeille en vol"></div>
    <h2 class="product-name">Miel de Kolvera</h2>
    <p class="product-swahili">ASALI YA KOLVERA</p>
    <p class="producer-brand"><span class="dot"></span>TUMSOA</p>
    <p class="product-origin">Miel Bio des plateaux de Kolvera<br>issue du Ranch de Kolvera</p>
    <p class="volume"><span class="rule"></span>660ml<span class="rule"></span></p>
  </section>

</main>
</body>
</html>
```